Financial Coaching biz needs modern service presentation menu

We need a PowerPoint presentation document with a modern, easy-to-read layout to share with potential clients.

I have a website under development that can be used as a reference www.brightledgerhub.com.

We'd like the doc to be simple to edit because services and verbiage will likely be modified periodically.

Two logo variations have been included.

Target Market(s)

Gen X, Gen Y, and Millienials

Industry/Entity Type

Financial Planning

Colors
85cae6
cadf82
ffffff
dddddd
cfcfcf
cee9f5

```html
<!DOCTYPE html>
<html lang="en">
<head>
<meta charset="utf-8">
<title>BrightLedger Hub – Service Menu Slides</title>
<link href="https://fonts.googleapis.com/css2?family=Open+Sans:wght@400;600;700&family=Roboto+Condensed:wght@300;400;700&display=swap" rel="stylesheet">
<style>
:root{
  --stage:#707070;
  --blue:#29a9e1;
  --sky:#85cae6;
  --ice:#cee9f5;
  --lime:#cadf82;
  --green:#9cc54a;
  --white:#ffffff;
  --light:#dddddd;
  --mid:#cfcfcf;
  --ink:#3a3a3a;
  --grey:#6d6d6d;
}
*{margin:0;padding:0;box-sizing:border-box}
html,body{width:1200px;height:1200px;overflow:hidden}
body{background:radial-gradient(ellipse at center,#8a8a8a 0%,var(--stage) 75%);font-family:"Open Sans",sans-serif;position:relative}
h1,h2,h3{font-weight:400}
.slide{position:absolute;width:494px;height:349px;overflow:hidden}
.slide-cover{left:90px;top:34px;background:radial-gradient(ellipse at 50% 55%,#f6f9fb 0%,#e2ecf2 60%,#c9dde8 100%)}
.slide-benefits{left:618px;top:34px;background:linear-gradient(115deg,#6f8e8e 0%,#8eaaa9 45%,#9fbfca 100%)}
.slide-guarantee{left:90px;top:425px;background:linear-gradient(120deg,#9fc846 0%,#b3d46a 55%,#c7e08a 100%)}
.slide-services{left:618px;top:425px;background:linear-gradient(135deg,#c9d5dc 0%,#b8ccd6 55%,#a9c6d6 100%)}
.slide-compare{left:354px;top:812px;background:linear-gradient(150deg,#c6e4ee 0%,#bfe0ec 50%,#a8d6ea 100%)}

.faint-art{position:absolute;border-radius:50%;background:radial-gradient(ellipse,rgba(255,255,255,.35),rgba(255,255,255,0) 70%)}

.brand{position:absolute;display:flex;align-items:center;gap:4px;font-family:"Roboto Condensed",sans-serif;font-weight:700;text-transform:uppercase;line-height:1}
.brand-dot{border-radius:50%;background:var(--white)}
.brand-mini{right:30px;top:34px;font-size:9px;color:var(--white)}
.brand-mini .brand-dot{width:10px;height:10px}
.brand-cover{left:0;right:0;top:36px;justify-content:center;font-size:20px;color:#2eae7a;gap:7px}
.brand-cover .brand-dot{width:22px;height:22px;background:#b8c2c6}

.rule{position:absolute;height:1px}

.cover-head{position:absolute;left:0;right:0;top:122px;text-align:center;font-family:"Roboto Condensed",sans-serif}
.cover-head h1{font-weight:700;font-size:21px;color:var(--blue);letter-spacing:.2px}
.cover-head p{font-weight:300;font-size:21px;color:var(--grey);line-height:26px;margin-top:2px}
.cover-band{position:absolute;left:0;right:0;top:319px;height:15px;background:var(--blue);display:flex;justify-content:space-between;align-items:center;padding:0 14px;font-size:8px;color:var(--white)}
.cover-band-under{position:absolute;left:0;right:0;top:334px;bottom:0;background:#dce9f0}

.ben-title{position:absolute;left:18px;top:26px;font-family:"Open Sans",sans-serif;font-weight:400;font-size:13px;color:var(--white)}
.ben-title span{color:var(--lime)}
.ben-list{position:absolute;left:19px;top:76px;width:430px}
.ben-item{margin-bottom:10px}
.ben-item h3{font-family:"Open Sans",sans-serif;font-weight:400;font-size:10px;color:var(--lime);text-transform:uppercase;line-height:13px}
.ben-item p{font-size:9.8px;line-height:13px;color:var(--white)}

.foot{position:absolute;left:0;right:0;top:317px;height:20px}
.foot-band{position:absolute;top:3px;height:14px;background:var(--blue)}
.foot-tab{position:absolute;top:0;height:20px;font-size:8px;display:flex;align-items:center}

.guar-title{position:absolute;left:16px;top:22px;font-size:17px;font-weight:400;color:var(--white)}
.guar-title b{font-weight:700}
.guar-body{position:absolute;left:17px;top:68px;width:370px;font-size:9.6px;line-height:13px;color:#2f3a25}
.guar-body p{margin-bottom:12px;text-align:justify}
.guar-close{position:absolute;left:17px;top:234px;font-size:14.5px;color:#2f3a25}

.svc-table{position:absolute;left:23px;top:72px;width:451px;height:194px;display:grid;grid-template-columns:repeat(5,1fr);gap:0 1px;background:var(--blue)}
.svc-col{background:rgba(236,241,244,.8);display:flex;flex-direction:column;align-items:center}
.svc-head{width:100%;height:37px;background:var(--blue);color:var(--white);font-family:"Roboto Condensed",sans-serif;font-weight:700;font-size:7px;text-align:center;padding-top:9px;line-height:9px}
.svc-icon{width:22px;height:22px;border-radius:50%;background:var(--blue);border:2px solid var(--white);margin-top:-8px;display:flex;align-items:center;justify-content:center}
.svc-icon i{width:8px;height:9px;border:1.5px solid var(--white);border-radius:1px}
.svc-col p{font-size:7.2px;line-height:9.6px;color:var(--grey);text-align:center;padding:0 6px;margin-top:8px}
.svc-note{position:absolute;left:25px;top:284px;font-size:7px;color:#3d4a52}

.cmp-heads{position:absolute;top:56px;left:0;right:0;font-family:"Roboto Condensed",sans-serif;font-weight:700;font-size:6.5px;color:#4c5a62;text-transform:uppercase}
.cmp-heads span{position:absolute;transform:translateX(-50%);white-space:nowrap}
.cmp-row{position:absolute;left:19px;width:444px;height:34px;font-size:6.8px;font-weight:700;color:#4c5a62;text-transform:uppercase;padding-left:9px;display:flex;align-items:center}
.cmp-row.alt{background:rgba(255,255,255,.55)}
</style>
</head>
<body>

<section class="slide slide-cover">
  <div class="faint-art" role="img" aria-label="Faint mascot artwork in the background" style="left:40px;top:60px;width:420px;height:300px"></div>
  <div class="brand brand-cover"><span class="brand-dot"></span>BrightLedger Hub</div>
  <div class="cover-head">
    <h1>HELPING OUR CLIENTS</h1>
    <p>NTELLIGENTLY AND STRATEGICALLY<br>MANAGE THEIR FINANCES.</p>
  </div>
  <div class="cover-band"><span>w</span><span>w</span><span>w</span><span>.</span><span>b</span><span>r</span><span>i</span><span>g</span><span>h</span><span>t</span><span>l</span><span>e</span><span>d</span><span>g</span><span>e</span><span>r</span><span>h</span><span>u</span><span>b</span><span>.</span><span>c</span><span>o</span><span>m</span></div>
  <div class="cover-band-under"></div>
</section>

<section class="slide slide-benefits">
  <div class="faint-art" role="img" aria-label="Faint mascot artwork in the background" style="left:220px;top:150px;width:300px;height:220px"></div>
  <h2 class="ben-title">SPECIAL BENEFITS FOR FULL <span>PARTNERSHIP</span></h2>
  <div class="rule" style="left:18px;top:46px;width:352px;background:var(--lime)"></div>
  <div class="brand brand-mini"><span class="brand-dot"></span>BrightLedger Hub</div>
  <div class="ben-list">
    <div class="ben-item"><h3>Savings Builder</h3><p>Tired of the banks not paying interest? Want to put money away but you're afraid you don't have enough to start with. Well we pay a CASH BONUS for staying on track with your savings goal, no matter how small the amount</p></div>
    <div class="ben-item"><h3>In-Person Budget Buddy Service</h3><p>You get a professional negotiator at the table with you for major purchases. You can also take your strategist with you to the mall or grocer to help you stay on budget</p></div>
    <div class="ben-item"><h3>Coupon Companion</h3><p>Don't have time or feel like clipping coupons, we have an EXTREME COUPONER on staff to notify clients when great deals come up</p></div>
    <div class="ben-item"><h3>VIP Seminar Access</h3><p>Learn about credit, home buying, budgeting, taxes, negotiating, refinancing loans, starting a business, and more in an intimate, small group setting</p></div>
  </div>
  <div class="foot">
    <div class="foot-band" style="left:170px;right:0"></div>
    <div class="foot-tab" style="left:0;width:180px;background:var(--lime);clip-path:polygon(0 0,100% 0,94% 100%,0 100%);padding-left:16px;color:#3f4a2a">www.brightledgerhub.com</div>
  </div>
</section>

<section class="slide slide-guarantee">
  <div class="faint-art" role="img" aria-label="Faint mascot artwork in the background" style="left:300px;top:20px;width:260px;height:300px"></div>
  <h2 class="guar-title"><b>100%</b> SATISFACTION <b>GUARANTEE</b></h2>
  <div class="rule" style="left:16px;top:46px;width:352px;background:rgba(255,255,255,.7)"></div>
  <div class="brand brand-mini"><span class="brand-dot"></span>BrightLedger Hub</div>
  <div class="guar-body">
    <p>We provide a FREE CONSULTATION and conduct a full assessment before we take on any new client.</p>
    <p>Therefore, prospective clients find out upfront if we can actually help them. We pride ourselves on being good corporate citizens as well. For every new household we sign, we commit to providing free service to household below the poverty line.</p>
    <p>Our promise is that we won't take on or charge a client a single cent unless we are ABSOLUTELY SURE we can add value. Our company is fundamentally built upon the service and the help we provide.</p>
  </div>
  <p class="guar-close">So if we can't help you, we won't charge you.&nbsp; PERIOD.</p>
  <div class="foot">
    <div class="foot-band" style="left:0;right:160px"></div>
    <div class="foot-tab" style="right:0;width:180px;background:#eef0ec;clip-path:polygon(6% 0,100% 0,100% 100%,0 100%);padding-left:31px;color:#3a3a3a">www.brightledgerhub.com</div>
  </div>
</section>

<section class="slide slide-services">
  <div class="rule" style="left:27px;top:46px;width:343px;background:var(--lime)"></div>
  <div class="brand brand-mini"><span class="brand-dot"></span>BrightLedger Hub</div>
  <div class="svc-table">
    <div class="svc-col"><div class="svc-head">Monetary Action Plan</div><span class="svc-icon"><i></i></span><p>Establish full-year plan for spending and saving, including major purchases or events</p></div>
    <div class="svc-col"><div class="svc-head">Budgeting Service</div><span class="svc-icon"><i></i></span><p>Unlimited consultations to determine holes and waste in spending</p><p>Client choice from multiple budgeting strategies to determine best personal fit</p></div>
    <div class="svc-col"><div class="svc-head">BrightLedger<br>Credit-Ed Service</div><span class="svc-icon"><i></i></span><p>Personalized assessment with ALL 3 bureaus</p><p>All Documentation provided for future use and personal records</p><p>Provide tools, knowledge, and strategy to prevent future missteps</p></div>
    <div class="svc-col"><div class="svc-head">Asset Advocate</div><span class="svc-icon"><i></i></span><p>Complimentary Rental and Mortgage Assessment</p><p>Quarterly Insurance Assessment</p><p>Quarterly Utility Assessment</p></div>
    <div class="svc-col"><div class="svc-head">Tax Preparation</div><span class="svc-icon"><i></i></span><p>Free prior year return review and amendment filing</p><p>Guarantee best price</p><p>Partnership discount applied with all future filings</p></div>
  </div>
  <p class="svc-note">Starbursts: IN-PERSON BUDGET BUDDY SERVICE, SAVINGS BUILDER, COUPON COMPANION, FREE VIP SEMINAR ACCESS, and more!!!</p>
  <div class="foot">
    <div class="foot-band" style="left:0;right:170px"></div>
    <div class="foot-tab" style="right:0;width:180px;background:var(--lime);clip-path:polygon(6% 0,100% 0,100% 100%,0 100%);padding-left:30px;color:#3f4a2a">www.brightledgerhub.com</div>
  </div>
</section>

<section class="slide slide-compare">
  <div class="faint-art" role="img" aria-label="Faint mascot artwork in the background" style="left:0;top:0;width:260px;height:200px"></div>
  <div class="rule" style="left:21px;top:36px;width:345px;background:var(--blue)"></div>
  <div class="brand brand-mini" style="top:26px;color:var(--white)"><span class="brand-dot"></span>BrightLedger Hub</div>
  <div class="cmp-heads">
    <span style="left:179px">TaxHarbor</span>
    <span style="left:231px">FileSwift</span>
    <span style="left:287px">PlanNest</span>
    <span style="left:349px">CreditFair Legal</span>
    <span style="left:431px">BrightLedger Hub</span>
  </div>
  <div class="cmp-row alt" style="top:72px">Tax Preparation</div>
  <div class="cmp-row" style="top:106px">Credit Education</div>
  <div class="cmp-row alt" style="top:140px">Budgeting Service</div>
  <div class="cmp-row" style="top:174px">Asset Advocacy</div>
  <div class="cmp-row alt" style="top:206px">Monetary Action Plan</div>
  <div class="cmp-row" style="top:240px">Savings Builder</div>
  <div class="cmp-row alt" style="top:275px">In-Person Face to Face Service</div>
  <svg width="494" height="349" viewBox="0 0 494 349" style="position:absolute;left:0;top:0" aria-hidden="true">
    <defs><path id="tk" d="M0 5 L4 9 L12 0" fill="none" stroke="#29a9e1" stroke-width="2.2" stroke-linecap="round" stroke-linejoin="round"/></defs>
    <use href="#tk" x="173" y="85"/><use href="#tk" x="226" y="85"/><use href="#tk" x="427" y="85"/>
    <use href="#tk" x="344" y="117"/><use href="#tk" x="427" y="117"/>
    <use href="#tk" x="281" y="151"/><use href="#tk" x="427" y="151"/>
    <use href="#tk" x="427" y="184"/>
    <use href="#tk" x="427" y="215"/>
    <use href="#tk" x="427" y="249"/>
    <use href="#tk" x="173" y="284"/><use href="#tk" x="427" y="284"/>
  </svg>
  <div class="foot" style="top:320px">
    <div class="foot-band" style="left:0;right:170px"></div>
    <div class="foot-tab" style="right:0;width:180px;background:#e4e9ec;clip-path:polygon(6% 0,100% 0,100% 100%,0 100%);padding-left:28px;color:#3a3a3a">www.brightledgerhub.com</div>
  </div>
</section>

</body>
</html>
```